Edgey T-shirt company needs a "Look book" cataloguing current products

We require a look book to approach retail stores with our current season's products. Needs to be eye catching but not distracting to the main product.

Target Market(s)

teen - mid 30s who like to wear things that maybe controversial or expresses a statement.
Also targets an audience who have a crude sense of humor, and likes to dress fun.

Industry/Entity Type

Retail

Requirements
Must have
• - Design template so I can drop photos onto page (made updateable).
- 8.5" x 5.5" landscape format (Half letter size)
- Designed in such a way to be reusable every season
- Similar feel as our website: www.brovikan.com
- Suggested retail price
- Have a space where I can edit product descriptions (material, weight, type etc)
- First page(s) to be an overview of all the styles in small boxes
- The rest of the pages with a single style per page, to be bound into a horizontal flip book.

```html
<!DOCTYPE html>
<html lang="en">
<head>
<meta charset="utf-8">
<title>Look Book – Style Page</title>
<link rel="stylesheet" href="https://fonts.googleapis.com/css2?family=Amatic+SC:wght@700&display=swap">
<style>
  :root {
    --page-bg: #ffffff;
    --ink-black: #000000;
    --brand-red: #ff0000;
    --paper-white: #ffffff;
    --shirt-teal: #2cc4de;
    --shirt-teal-dark: #1aa9c2;
    --sketch-grey: #e4e4e4;
    --sketch-grey-dark: #c9c9c9;
  }
  html, body {
    margin: 0;
    padding: 0;
    overflow: hidden;
    background: var(--page-bg);
  }
  .page {
    position: relative;
    width: 1200px;
    height: 1000px;
    overflow: hidden;
    background: var(--page-bg);
    font-family: "Amatic SC", cursive;
  }
  .price-panel {
    position: absolute;
    left: 0;
    top: 0;
  }
  .price-copy {
    position: absolute;
    left: 40px;
    top: 170px;
    width: 500px;
    text-align: center;
    color: var(--paper-white);
  }
  .price-headline {
    margin: 0;
    font-size: 92px;
    line-height: 74px;
    letter-spacing: 3px;
  }
  .sizes {
    margin: 28px 0 0;
    font-size: 42px;
    line-height: 40px;
    letter-spacing: 1px;
  }
  .description-box {
    position: absolute;
    left: 90px;
    top: 558px;
    width: 467px;
    height: 237px;
    background: var(--paper-white);
  }
  .description-title {
    position: absolute;
    left: 38px;
    top: 18px;
    margin: 0;
    color: var(--brand-red);
    font-size: 66px;
    line-height: 66px;
    letter-spacing: 2px;
  }
  .product-photo {
    position: absolute;
    left: 617px;
    top: 148px;
    width: 423px;
    height: 695px;
    background: linear-gradient(180deg, var(--shirt-teal) 0%, var(--shirt-teal-dark) 100%);
  }
  .side-strip {
    position: absolute;
    left: 1040px;
    top: 148px;
    width: 132px;
    height: 695px;
    background: linear-gradient(90deg, var(--sketch-grey) 0%, var(--paper-white) 50%, var(--sketch-grey-dark) 100%);
  }
  .colour-note {
    position: absolute;
    left: 1058px;
    top: 420px;
    width: 34px;
    height: 212px;
    border: 4px solid var(--brand-red);
    border-radius: 6px;
    background: var(--paper-white);
    display: flex;
    align-items: center;
    justify-content: center;
  }
  .colour-note span {
    writing-mode: vertical-rl;
    color: var(--ink-black);
    font-size: 24px;
    letter-spacing: 1px;
    white-space: nowrap;
  }
</style>
</head>
<body>
  <main class="page">
    <svg class="price-panel" width="600" height="830" viewBox="0 0 600 830">
      <defs>
        <clipPath id="panel-area">
          <rect x="27" y="148" width="568" height="672"/>
        </clipPath>
      </defs>
      <rect class="red-panel" x="52" y="295" width="543" height="525" fill="var(--brand-red)"/>
      <g clip-path="url(#panel-area)">
        <circle class="price-circle-ring" cx="310" cy="222" r="298" fill="var(--paper-white)"/>
        <circle class="price-circle" cx="310" cy="222" r="288" fill="var(--ink-black)"/>
      </g>
    </svg>

    <div class="price-copy">
      <h1 class="price-headline">Only<br>$40.00!</h1>
      <p class="sizes">Available Sizes: unisex<br>XS S M L XL</p>
    </div>

    <section class="description-box">
      <h2 class="description-title">Descrption</h2>
    </section>

    <div class="product-photo" role="img" aria-label="Product photo: model wearing the turquoise graphic tank top"></div>
    <div class="side-strip" role="img" aria-label="Decorative grey sketch pattern strip"></div>

    <div class="colour-note"><span>Also Available in Red!</span></div>
  </main>
</body>
</html>
```